Business Card Design Project

I run holistic health workshops, speaking engagements, group and 1on1 coaching, cooking classes, and am a speaker and presenter on holistic health topics.

I would like professionally designed business cards using the attached logo. I would like the reverse of the cards to use the leaf pattern blown up large across the back of the card as the design. I'd also like to use the words "mind.body.spirit.nutrition" across the backside of the cards.

The front of the cards should contain the following contact details:
Megan Thorsby-Kell
Founder & President
The Harwick Advisory Group
+61 477 392 604
theharwickadvisorygroup@mailbrook.example

Target Market(s)

Corporate HR, Health & wellness businesses, upmarket spas, other businesses in the holistic health & wellness fields looking for a speaker/presenter/workshop leader

Industry/Entity Type

Cooking

Requirements
Must have
• Must use the attached design; must use earth tones in line with the logo (browns/greens/blues/tans)

```html
<!DOCTYPE html>
<html lang="en">
<head>
<meta charset="utf-8">
<title>Harwick Group – Business Card</title>
<link href="https://fonts.googleapis.com/css2?family=Didact+Gothic&family=Open+Sans:wght@400;700&display=swap" rel="stylesheet">
<style>
  :root {
    --canvas-bg: #e5f0d8;
    --card-bg: #ffffff;
    --leaf-green: #8cc63f;
    --mid-green: #5aa743;
    --deep-green: #13744a;
    --charcoal: #4a4a46;
    --band-dark: #4f4f4b;
    --shadow: rgba(60, 70, 50, 0.22);
  }
  * { margin: 0; padding: 0; box-sizing: border-box; }
  html, body {
    width: 1200px;
    height: 1000px;
    overflow: hidden;
    background: var(--canvas-bg);
  }
  .canvas {
    position: relative;
    width: 1200px;
    height: 1000px;
  }
  .card {
    position: absolute;
    background: var(--card-bg);
    overflow: hidden;
    box-shadow: 2px 3px 6px var(--shadow);
  }

  /* Front */
  .card--front {
    left: 288px; top: 74px;
    width: 683px; height: 419px;
  }
  .front__glow {
    position: absolute;
    inset: 0;
    background:
      radial-gradient(ellipse 190px 230px at 20px 330px, var(--deep-green) 0%, rgba(19,116,74,0.6) 45%, rgba(19,116,74,0) 100%),
      radial-gradient(ellipse 240px 300px at 60px 170px, var(--leaf-green) 0%, rgba(140,198,63,0.75) 40%, rgba(140,198,63,0) 100%),
      radial-gradient(ellipse 300px 380px at 40px 260px, rgba(90,167,67,0.9) 0%, rgba(90,167,67,0.4) 55%, rgba(90,167,67,0) 100%);
  }
  .brand {
    position: absolute;
    right: 56px;
    top: 168px;
    display: flex;
    align-items: center;
    gap: 16px;
  }
  .brand__dot {
    width: 26px; height: 26px;
    border-radius: 50%;
    background: var(--leaf-green);
  }
  .brand__name {
    font-family: "Didact Gothic", sans-serif;
    font-size: 52px;
    line-height: 1;
    color: var(--charcoal);
    letter-spacing: 1px;
  }

  /* Back */
  .card--back {
    left: 285px; top: 533px;
    width: 680px; height: 415px;
  }
  .back__band {
    position: absolute;
    left: 0; right: 0; bottom: 0;
    height: 220px;
    background: linear-gradient(to bottom, rgba(255,255,255,0) 0%, #dcdcda 30%, #8a8a86 60%, var(--band-dark) 85%);
  }
  .back__leaves {
    position: absolute;
    left: 0; top: 0;
    width: 330px; height: 280px;
    border-radius: 0 0 160px 0;
    background:
      radial-gradient(ellipse 70px 140px at 95px 90px, var(--deep-green) 0%, rgba(19,116,74,0.85) 60%, rgba(19,116,74,0) 100%),
      radial-gradient(ellipse 180px 150px at 160px 140px, var(--mid-green) 0%, rgba(90,167,67,0.7) 55%, rgba(140,198,63,0.25) 100%),
      linear-gradient(135deg, var(--leaf-green), #b6d98a);
  }
  .contact {
    position: absolute;
    right: 35px;
    text-align: right;
    font-family: "Open Sans", sans-serif;
    color: var(--charcoal);
  }
  .contact--identity { top: 74px; }
  .contact__name {
    font-weight: 700;
    font-size: 27px;
    color: var(--leaf-green);
    letter-spacing: 0.5px;
  }
  .contact__role {
    font-weight: 700;
    font-size: 23px;
    margin-top: 2px;
  }
  .contact__company {
    font-family: "Didact Gothic", sans-serif;
    font-size: 21px;
    margin-top: 2px;
  }
  .contact--reach { top: 252px; }
  .contact__phone {
    font-family: "Didact Gothic", sans-serif;
    font-size: 20px;
  }
  .contact__email {
    font-weight: 700;
    font-size: 17px;
    margin-top: 4px;
  }
  .tagline {
    position: absolute;
    right: 32px;
    bottom: 26px;
    font-family: "Didact Gothic", sans-serif;
    font-size: 47px;
    line-height: 1;
    color: #ffffff;
    letter-spacing: 0.5px;
  }
  .tagline__accent { color: var(--leaf-green); }
</style>
</head>
<body>
<main class="canvas">
  <section class="card card--front" aria-label="Card front">
    <div class="front__glow"></div>
    <div class="brand">
      <span class="brand__dot"></span>
      <span class="brand__name">Harwick Group</span>
    </div>
  </section>

  <section class="card card--back" aria-label="Card back">
    <div class="back__band"></div>
    <div class="back__leaves" role="img" aria-label="Enlarged leaf motif from the brand symbol"></div>
    <div class="contact contact--identity">
      <p class="contact__name">Megan Thorsby-Kell</p>
      <p class="contact__role">President</p>
      <p class="contact__company">the harwick advisory group</p>
    </div>
    <div class="contact contact--reach">
      <p class="contact__phone">+61 477 392 604</p>
      <p class="contact__email">theharwickadvisorygroup@mailbrook.example</p>
    </div>
    <p class="tagline">mind.<span class="tagline__accent">body</span>.spirit.<span class="tagline__accent">nutrition</span></p>
  </section>
</main>
</body>
</html>
```